Dance school needs a poster to promote our annual concert

I have a dance school called 'The Marcella Dunwoody Dancers'
See designs from previous years
This year's concert theme is Brant Holloway animation movies
The title of the concert is "glimmeRa"
Dance items will be choreographed to; “Quiet Orchard”, Copper Heron”, “The Nine Lanterns”, “The Fox Regent”, “Temrik”, “Willow & the Warden” & “Pipsqueeve”.
I need a colorful A4 (portrait) poster promoting the concert.

Target Market(s)

Families of students & dance community

Industry/Entity Type

Dance Studio

Font styles to use
Other font styles liked:
• "Mistral" for my my name (see examples supplied)

Colors

Designer to choose colors to be used in the design.

Requirements
Must have
• Must Have:
• - The poster must include the following information:
• 'The Marcella Dunwoody Dancers'
• presents
• "glimmeRa"
• (Font for my name is "Mistral")
• Saturday 18th November 2017
• Corbett Hall,
• Halverd Grammar Elmstead.

```html
<!DOCTYPE html>
<html lang="en">
<head>
<meta charset="utf-8">
<title>glimmeRa — The Marcella Dunwoody Dancers</title>
<link href="https://fonts.googleapis.com/css2?family=Kaushan+Script&family=Roboto+Condensed:wght@400;500&family=Almendra:wght@700&display=swap" rel="stylesheet">
<style>
  :root {
    --deep-violet: #3a1a8f;
    --star-yellow: #fff200;
    --white: #ffffff;
    --title-fill-top: #b25cf0;
    --title-fill-bottom: #7a1fd1;
    --wand-glow: #ffe23a;
    --wand-gold: #f5b400;
  }
  * { margin: 0; padding: 0; box-sizing: border-box; }
  html, body { width: 848px; height: 1200px; overflow: hidden; background: var(--deep-violet); }
  .poster {
    position: relative;
    width: 848px;
    height: 1200px;
    overflow: hidden;
    background:
      radial-gradient(ellipse 420px 260px at 420px 620px, rgba(80,70,255,0.75), transparent 70%),
      radial-gradient(ellipse 380px 300px at 120px 180px, rgba(170,40,200,0.55), transparent 70%),
      radial-gradient(ellipse 360px 280px at 760px 140px, rgba(150,40,190,0.5), transparent 70%),
      radial-gradient(ellipse 500px 260px at 620px 1060px, rgba(200,60,190,0.7), transparent 70%),
      radial-gradient(ellipse 420px 240px at 120px 1020px, rgba(190,60,190,0.55), transparent 70%),
      linear-gradient(180deg, #5a1f9e 0%, #4930c9 45%, #5a2bb8 70%, #8a2aa6 100%);
  }
  .sparkles { position: absolute; inset: 0; }
  .logo {
    position: absolute;
    top: 96px; left: 0; width: 100%;
    text-align: center;
    font-family: "Roboto Condensed", sans-serif;
    font-weight: 500;
    font-size: 44px;
    letter-spacing: 0.08em;
    color: var(--star-yellow);
  }
  .school-name {
    position: absolute;
    top: 268px; left: 0; width: 100%;
    text-align: center;
    font-family: "Kaushan Script", cursive;
    font-weight: 400;
    font-size: 50px;
    color: var(--star-yellow);
    transform: rotate(-2deg);
    white-space: nowrap;
  }
  .presents {
    position: absolute;
    top: 330px; left: 0; width: 100%;
    text-align: center;
    font-family: "Roboto Condensed", sans-serif;
    font-size: 40px;
    letter-spacing: 0.55em;
    padding-left: 0.55em;
    color: var(--white);
  }
  .mist {
    position: absolute;
    left: 0; top: 720px; width: 848px; height: 230px;
    background:
      radial-gradient(ellipse 420px 80px at 300px 110px, rgba(240,220,255,0.55), transparent 75%),
      radial-gradient(ellipse 380px 70px at 640px 125px, rgba(230,150,240,0.5), transparent 75%);
  }
  .wand-art {
    position: absolute;
    left: 716px; top: 484px;
    width: 132px; height: 170px;
    background: radial-gradient(ellipse 60px 60px at 50px 46px, rgba(255,226,58,0.85), rgba(245,180,0,0.35) 60%, transparent 100%);
  }
  .title { position: absolute; left: 0; top: 440px; }
  .event-info {
    position: absolute;
    top: 1004px; left: 0; width: 100%;
    text-align: center;
    font-family: "Roboto Condensed", sans-serif;
    font-size: 44px;
    line-height: 1.1;
    text-transform: uppercase;
  }
  .event-date { color: var(--white); }
  .event-date sup { font-size: 0.45em; vertical-align: 1.1em; line-height: 0; }
  .event-venue { color: var(--star-yellow); }
</style>
</head>
<body>
<main class="poster">
  <svg class="sparkles" width="848" height="1200" aria-hidden="true">
    <g fill="#ffffff" opacity="0.85">
      <circle cx="573" cy="50" r="2"/><circle cx="768" cy="170" r="2.5"/>
      <circle cx="60" cy="420" r="1.5"/><circle cx="470" cy="430" r="1.5"/>
      <circle cx="834" cy="378" r="2"/><circle cx="660" cy="320" r="2"/>
      <circle cx="120" cy="1130" r="1.5"/><circle cx="640" cy="990" r="1.5"/>
      <circle cx="300" cy="960" r="1"/><circle cx="780" cy="1150" r="1.5"/>
    </g>
    <g fill="#ff5fa8" opacity="0.5">
      <circle cx="80" cy="96" r="10"/><circle cx="358" cy="6" r="8"/>
      <circle cx="805" cy="395" r="10"/><circle cx="640" cy="397" r="7"/>
      <circle cx="538" cy="140" r="7"/><circle cx="250" cy="260" r="6"/>
    </g>
  </svg>

  <div class="logo">MDD</div>
  <h1 class="school-name">The Marcella Dunwoody Dancers</h1>
  <p class="presents">PRESENTS</p>

  <div class="mist" role="img" aria-label="Soft swirling white and pink smoke beneath the title"></div>
  <div class="wand-art" role="img" aria-label="Glowing golden star-tipped magic wand beside the title"></div>

  <svg class="title" width="848" height="420" viewBox="0 0 848 420" role="img" aria-label="glimmeRa">
    <defs>
      <linearGradient id="titleFill" x1="0" y1="0" x2="0" y2="1">
        <stop offset="0" stop-color="var(--title-fill-top)"/>
        <stop offset="1" stop-color="var(--title-fill-bottom)"/>
      </linearGradient>
    </defs>
    <text x="424" y="336" text-anchor="middle" textLength="750" lengthAdjust="spacingAndGlyphs"
          font-family="Almendra, serif" font-weight="700" font-size="280"
          fill="url(#titleFill)" stroke="#ffffff" stroke-width="5" paint-order="stroke">glimmeRa</text>
  </svg>

  <section class="event-info">
    <p class="event-date">Saturday, 18<sup>th</sup> November 2017</p>
    <p class="event-venue">Corbett Hall,</p>
    <p class="event-venue">Halverd Grammar Elmstead</p>
  </section>
</main>
</body>
</html>
```